Tarvell homes and renovations business card design.

Would like some new card designs utilizing my new logo that look professional. I am open to different colors on the logo or utilize the same ones we have. I like the original concept but would like to see some fresh ideas and build on what we have already done.

Target Market(s)

Custom home building industry, Real estate sales, Renovation projects.

Industry/Entity Type

Home Builder

Contact Information for Business Card

Tarvell Homes and Renovations
2871 162nd Street
Ridgemoor, Westvale
T0L3P0
Home : 403- 555-0187 Cell: 403- 555-0243

My info is : Gus Tarvell, President and CEO
email: tarvellhomes@quillmail.example
Website: tarvellhomes.example

Requirements
Must have
• Must Use my new logo design. I am open to different colors on the logo or utilize the same ones in the existing design. I can upload the original logo design if needed.

```html
<!DOCTYPE html>
<html lang="en">
<head>
<meta charset="utf-8">
<title>Tarvell Homes and Renovations – Business Card</title>
<link href="https://fonts.googleapis.com/css2?family=Open+Sans:wght@400;600;700&display=swap" rel="stylesheet">
<style>
  :root {
    --page: #e9e6e1;
    --card: #333333;
    --gold: #c9a45a;
    --gold-bright: #f2b81c;
    --ink: #f1f1f1;
    --muted: #8a8a8a;
  }
  * { margin: 0; padding: 0; box-sizing: border-box; }
  html, body { width: 1200px; height: 800px; overflow: hidden; }
  body {
    background: var(--page);
    font-family: "Open Sans", Arial, sans-serif;
    position: relative;
  }
  .card {
    position: absolute;
    width: 525px;
    height: 300px;
    background: var(--card);
    border-radius: 18px;
    box-shadow: 0 10px 28px rgba(0,0,0,.25);
    overflow: hidden;
  }
  .card--front { left: 50px; top: 250px; }
  .card--back { left: 625px; top: 250px; }

  .wordmark {
    color: var(--gold);
    font-weight: 700;
    line-height: 1;
    text-align: center;
  }
  .card--front .wordmark {
    position: absolute;
    left: 0; right: 0; top: 105px;
  }
  .card--front .wordmark__name { display: block; font-size: 58px; letter-spacing: 2px; }
  .card--front .wordmark__tag { display: block; font-size: 15px; letter-spacing: 2px; margin-top: 8px; text-transform: uppercase; }

  .card--back .wordmark {
    position: absolute;
    right: 28px; top: 34px;
    text-align: left;
  }
  .card--back .wordmark__name { display: block; font-size: 32px; letter-spacing: 1px; }
  .card--back .wordmark__tag { display: block; font-size: 8.5px; letter-spacing: 1px; margin-top: 4px; text-transform: uppercase; }

  .person {
    position: absolute;
    left: 0; top: 108px;
    padding-left: 26px;
    border-left: 7px solid var(--gold-bright);
  }
  .person__name { font-size: 20px; font-weight: 600; color: var(--muted); line-height: 1.1; }
  .person__title { font-size: 17px; color: var(--gold-bright); line-height: 1.15; }

  .contacts {
    position: absolute;
    left: 33px; top: 166px;
    list-style: none;
    font-size: 12px;
    color: var(--ink);
  }
  .contacts li {
    display: flex;
    align-items: flex-start;
    gap: 12px;
    line-height: 1.35;
    margin-bottom: 2px;
  }
  .contacts svg { width: 12px; height: 12px; flex: none; margin-top: 2px; fill: var(--gold-bright); }

  .accent-line {
    position: absolute;
    left: 0; top: 0;
    width: 525px; height: 300px;
  }
  .website {
    position: absolute;
    left: 33px; bottom: 6px;
    font-size: 13px;
    color: var(--gold-bright);
  }
</style>
</head>
<body>

  <section class="card card--front" aria-label="Card front">
    <div class="wordmark">
      <span class="wordmark__name">TARVELL</span>
      <span class="wordmark__tag">Homes and Renovations</span>
    </div>
  </section>

  <section class="card card--back" aria-label="Card back">
    <div class="wordmark">
      <span class="wordmark__name">TARVELL</span>
      <span class="wordmark__tag">Homes and Renovations</span>
    </div>

    <div class="person">
      <p class="person__name">Gus Tarvell</p>
      <p class="person__title">President and CEO</p>
    </div>

    <ul class="contacts">
      <li>
        <svg viewBox="0 0 12 12" aria-hidden="true"><path d="M6 0a4 4 0 0 0-4 4c0 3 4 8 4 8s4-5 4-8a4 4 0 0 0-4-4zm0 5.6A1.6 1.6 0 1 1 6 2.4a1.6 1.6 0 0 1 0 3.2z"/></svg>
        <span>2871 162nd Street<br>Ridgemoor, Westvale, T0L3P0</span>
      </li>
      <li>
        <svg viewBox="0 0 12 12" aria-hidden="true"><path d="M1 4c0-1.5 2-2.5 5-2.5S11 2.5 11 4v1H8.5V3.8h-5V5H1zM2.5 6h7l1 5h-9z"/></svg>
        <span>403- 555-0187</span>
      </li>
      <li>
        <svg viewBox="0 0 12 12" aria-hidden="true"><path d="M3 0h6v12H3zm1 1.2v8.3h4V1.2z"/></svg>
        <span>403- 555-0243</span>
      </li>
      <li>
        <svg viewBox="0 0 12 12" aria-hidden="true"><path d="M0 2h12v8H0zm1.2 1 4.8 3.6L10.8 3z"/></svg>
        <span>tarvellhomes@quillmail.example</span>
      </li>
    </ul>

    <svg class="accent-line" viewBox="0 0 525 300" aria-hidden="true">
      <polyline points="0,268 330,268 400,108 525,108" fill="none" stroke="#f2b81c" stroke-width="3"/>
      <polygon points="402,104 525,104 525,112 399,112" fill="#f2b81c"/>
    </svg>

    <p class="website">tarvellhomes.example</p>
  </section>

</body>
</html>
```